Rivet Athletic Supply Inc.

Need to create a website that is informational and has the ability to sell goods and services. Such as a custom t shirt designer where the user can upload and image to be displayed on the garmet. The sports we specialize in are basketball, football, and baseball.

Would like like:
Home Page
Locker Room Page:
Custom Uniforms Page
Custom Shirt Creator
Brands
About

Competitor websites are
lornfieldsportsco.example
qtv.example
wmdgear.example

```html
<!DOCTYPE html>
<html lang="en">
<head>
<meta charset="utf-8">
<title>Rivet Athletic Supply</title>
<link href="https://fonts.googleapis.com/css2?family=Poppins:wght@400;500;600;700&display=swap" rel="stylesheet">
<style>
:root{
  --blue:#2559a9;
  --blue-dark:#1e4d98;
  --red:#d23b3b;
  --ink:#2b2b2b;
  --muted:#555;
  --white:#fff;
  --line:#e7e7e7;
}
*{margin:0;padding:0;box-sizing:border-box}
html,body{width:1200px;height:5362px;overflow:hidden}
body{font-family:'Poppins',sans-serif;color:var(--ink);background:var(--white);position:relative}
.abs{position:absolute}
/* header */
.site-header{position:absolute;left:0;top:0;width:1200px;height:104px}
.brand-mark{position:absolute;left:68px;top:36px;display:flex;align-items:center;gap:10px;font-weight:700;font-size:21px;color:var(--blue);letter-spacing:.2px}
.brand-mark .sq{width:22px;height:22px;background:var(--red)}
.main-nav{position:absolute;top:56px;left:0;width:1200px;font-size:13px;color:#333}
.main-nav a{position:absolute;color:#333;text-decoration:none}
.main-nav a.active{color:var(--red);border:1px solid var(--red);padding:0 3px;margin-left:-4px;margin-top:-1px}
.util{position:absolute;top:13px;right:67px;display:flex;gap:8px;align-items:center}
.util .ic{width:28px;height:28px;border-radius:50%;background:var(--red);display:flex;align-items:center;justify-content:center}
.btn-contact{background:var(--blue);color:#fff;font-size:11px;font-weight:600;border-radius:14px;padding:6px 15px;margin-left:8px}
/* hero */
.hero{position:absolute;left:0;top:104px;width:1200px;height:842px;background:linear-gradient(180deg,#3a2a20 0%,#6a3b1c 35%,#a85a23 60%,#2c2620 100%)}
.hero-text{position:absolute;left:0;width:1200px;text-align:center;color:#fff}
.btn{display:inline-flex;align-items:center;gap:8px;border-radius:24px;color:#fff;font-weight:600;text-transform:uppercase}
.dots{position:absolute;top:724px;left:576px;display:flex;gap:8px}
.dots i{width:6px;height:6px;border-radius:50%;border:1px solid #fff;display:block}
.dots i:first-child{background:#fff}
/* headings */
.sec-title{position:absolute;left:0;width:1200px;text-align:center;color:var(--blue);font-weight:600;font-size:45px;letter-spacing:-.3px}
.sec-rule{position:absolute;width:84px;height:2px;background:var(--red);left:558px}
/* sports */
.sport{position:absolute;width:180px;text-align:center}
.sport .ball{width:180px;height:180px;border-radius:50%}
.sport p{margin-top:26px;font-size:22px;font-weight:600;color:#222}
/* locker */
.locker-photo{position:absolute;left:0;top:1497px;width:853px;height:560px;background:linear-gradient(120deg,#b8501f 0%,#e0762f 35%,#6b3b22 65%,#1f4b4f 100%)}
.circle{position:absolute;border-radius:50%}
.circle-body{position:absolute;color:#fff;text-align:center}
.circle-body p{font-size:13px;line-height:24px;text-align:justify;text-align-last:center}
/* uniform cards */
.u-card{position:absolute;width:316px;text-align:center}
.u-card .ph{width:316px;height:347px}
.u-card h3{margin-top:30px;font-size:15px;font-weight:600;color:var(--blue)}
.u-card p{font-size:12.5px;color:#444;line-height:16px;margin-top:6px}
.stars{color:#f2c200;font-size:11px;letter-spacing:1px;margin-top:6px}
.btn-sm{display:inline-block;background:var(--red);color:#fff;font-size:10.5px;font-weight:600;border-radius:14px;padding:5px 16px;margin-top:6px}
.pager{position:absolute;display:flex;gap:8px}
.pager span{width:34px;height:34px;border-radius:50%;display:flex;align-items:center;justify-content:center}
/* shirt creator */
.s-card{position:absolute;width:320px;height:509px;background:#fff;box-shadow:0 0 14px rgba(0,0,0,.12);text-align:center;padding:16px}
.s-card .ph{width:288px;height:300px}
.s-card h3{margin-top:28px;font-size:15px;font-weight:600;color:var(--blue)}
.s-card .mini{width:20px;height:2px;background:var(--blue);margin:10px auto}
.s-card p{font-size:12.5px;color:#444;line-height:16px}
.btn-blue{display:inline-block;background:var(--blue);color:#fff;font-size:11px;font-weight:600;border-radius:18px;padding:8px 24px;margin-top:18px}
/* brands */
.brand-box{position:absolute;top:4726px;width:152px;height:81px;background:#fff;box-shadow:0 0 12px rgba(0,0,0,.12);display:flex;align-items:center;justify-content:center;font-size:16px;font-weight:600;color:#333}
/* footer */
.site-footer{position:absolute;left:0;top:4923px;width:1200px;height:439px;background:var(--blue);color:#fff}
.f-head{position:absolute;font-size:19px;font-weight:600}
.f-rule{position:absolute;width:44px;height:2px;background:#fff}
.f-links{position:absolute;left:160px;top:163px;list-style:none;font-size:12.5px}
.f-links li{height:32px;display:flex;align-items:center;gap:12px}
.f-links li::before{content:"";width:5px;height:5px;border-radius:50%;background:#fff}
.f-contact{position:absolute;left:805px;font-size:12.5px;line-height:15px;display:flex;gap:14px}
.f-contact .ci{width:26px;height:26px;border:1px solid #fff;border-radius:4px;flex:none;display:flex;align-items:center;justify-content:center}
.social{position:absolute;top:258px;left:507px;display:flex;gap:12px}
.social span{width:38px;height:38px;border:2px solid #fff;border-radius:50%}
</style>
</head>
<body>

<header class="site-header">
  <div class="brand-mark"><span class="sq"></span>Rivet Athletic Supply</div>
  <nav class="main-nav">
    <a class="active" style="left:428px">Home</a>
    <a style="left:512px">Locker Room</a>
    <a style="left:646px">Custom Uniforms</a>
    <a style="left:810px">Custom Shirt Creator</a>
    <a style="left:998px">Brands</a>
    <a style="left:1093px">About</a>
  </nav>
  <div class="util">
    <span class="ic"><svg width="14" height="14" viewBox="0 0 14 14" fill="none" stroke="#fff" stroke-width="1.8"><circle cx="6" cy="6" r="4"/><path d="M9 9l3.5 3.5"/></svg></span>
    <span class="ic"><svg width="14" height="14" viewBox="0 0 14 14" fill="none" stroke="#fff" stroke-width="1.6"><circle cx="7" cy="5" r="2.6"/><path d="M2 13c1-3 9-3 10 0"/></svg></span>
    <span class="ic"><svg width="14" height="14" viewBox="0 0 14 14" fill="none" stroke="#fff" stroke-width="1.6"><path d="M1 2h2l2 7h7l1.5-5H4"/><circle cx="6" cy="12" r="1"/><circle cx="11" cy="12" r="1"/></svg></span>
    <span class="btn-contact">CONTACT US</span>
  </div>
</header>

<section class="hero" role="img" aria-label="Team of players in orange kits celebrating on a stadium pitch">
  <div class="hero-text" style="top:236px;font-size:22px;font-weight:600">Welcome To</div>
  <div class="hero-text" style="top:270px;font-size:124px;font-weight:700;line-height:150px;color:var(--red);letter-spacing:4px">RIVET</div>
  <div class="hero-text" style="top:460px;font-size:44px;font-weight:600">ATHLETIC SUPPLY</div>
  <div class="hero-text" style="top:526px;font-size:19px;line-height:24px">Lorem ipsum dolor sit amet, consectetur adipiscing elit, sed do<br>eiusmod tempor incididunt ut labore et dolore magna aliqua.</div>
  <div class="hero-text" style="top:602px"><span class="btn" style="background:var(--blue);font-size:17px;padding:12px 26px">Shop Now <svg width="16" height="12" viewBox="0 0 16 12" fill="none" stroke="#fff" stroke-width="1.5"><path d="M1 6h11M9 3l3 3-3 3"/><path d="M12 1h3v10h-3"/></svg></span></div>
  <div class="dots"><i></i><i></i><i></i><i></i></div>
</section>

<h2 class="sec-title" style="top:1016px">THE SPORTS WE SPECIALIZE</h2>
<div class="sec-rule" style="top:1090px"></div>
<div class="sport" style="left:265px;top:1144px"><div class="ball" role="img" aria-label="Football" style="background:radial-gradient(circle at 40% 35%,#fff 0%,#ddd 55%,#555 100%)"></div><p>FOOTBALL</p></div>
<div class="sport" style="left:508px;top:1144px"><div class="ball" role="img" aria-label="Basketball" style="background:radial-gradient(circle at 40% 35%,#f48a42 0%,#e2621c 60%,#8a3a10 100%)"></div><p>BASKETBALL</p></div>
<div class="sport" style="left:761px;top:1144px"><div class="ball" role="img" aria-label="Baseball" style="background:radial-gradient(circle at 40% 35%,#fff 0%,#eee 60%,#b9b9b9 100%)"></div><p>BASEBALL</p></div>

<div class="locker-photo" role="img" aria-label="Locker room shelves with orange basketballs"></div>
<div class="circle" style="left:586px;top:1501px;width:554px;height:554px;background:linear-gradient(135deg,#fff,#cfc8c0)"></div>
<div class="circle" style="left:599px;top:1514px;width:528px;height:528px;background:var(--blue)"></div>
<div class="circle-body" style="left:634px;top:1590px;width:456px">
  <h2 style="font-size:46px;font-weight:600;line-height:58px">LOCKER ROOM</h2>
  <div style="width:80px;height:2px;background:#fff;margin:26px auto 30px"></div>
  <p>Lorem ipsum dolor sit amet, consectetur adipiscing elit, sed do eiusmod tempor incididunt ut labore et dolore magna aliqua. Quis ipsum suspendisse ultrices gravida. Risus commodo viverra maecenas accumsan lacus vel facilisis. Lorem ipsum dolor sit amet, consectetur adipiscing elit, sed do eiusmod tempor incididunt ut labore et dolore magna aliqua. Quis ipsum suspendisse ultrices gravida. Risus commodo viverra maecenas accumsan lacus vel facilisis.</p>
  <div style="margin-top:30px"><span class="btn" style="background:var(--red);font-size:15px;padding:9px 22px">Know More ⇾</span></div>
</div>

<h2 class="sec-title" style="top:2162px">CUSTOM UNIFORMS</h2>
<div class="sec-rule" style="top:2238px"></div>
<div class="u-card" style="left:75px;top:2317px"><div class="ph" role="img" aria-label="Girls team in white and blue football kits" style="background:linear-gradient(180deg,#6f8a5a,#e9eef5 45%,#2d5fb0 80%,#f2f2f2)"></div><h3>CUSTOM UNIFORM 1</h3><p>Lorem ipsum dolor sit amet,<br>consectetur adipiscing elit, sed do</p><div class="stars">★★★★★</div><span class="btn-sm">SHOP NOW</span></div>
<div class="u-card" style="left:441px;top:2317px"><div class="ph" role="img" aria-label="Player in a yellow uniform holding a ball" style="background:linear-gradient(180deg,#0c0c0c,#1a1a1a 25%,#d9a01f 50%,#b07c12 80%,#111)"></div><h3>CUSTOM UNIFORM2</h3><p>Lorem ipsum dolor sit amet,<br>consectetur adipiscing elit, sed do</p><div class="stars">★★★★★</div><span class="btn-sm">SHOP NOW</span></div>
<div class="u-card" style="left:809px;top:2317px"><div class="ph" role="img" aria-label="Player in a red baseball jersey holding a basketball" style="background:linear-gradient(180deg,#eeeeee,#e7e7e7 25%,#c8333a 45%,#2f4f8f 75%,#e5e5e5)"></div><h3>CUSTOM UNIFORM 3</h3><p>Lorem ipsum dolor sit amet,<br>consectetur adipiscing elit, sed do</p><div class="stars">★★★★★</div><span class="btn-sm">SHOP NOW</span></div>
<div class="pager" style="left:556px;top:2885px"><span style="background:#ddd;color:#999">‹</span><span style="background:var(--blue);color:#fff">›</span></div>

<h2 class="sec-title" style="top:3006px">CUSTOM SHIRT CREATOR</h2>
<div class="sec-rule" style="top:3083px"></div>
<div class="s-card" style="left:85px;top:3141px"><div class="ph" role="img" aria-label="Yellow basketball jersey on a hanger" style="background:linear-gradient(180deg,#f3f3f3,#e8f53a 40%,#dbe630 80%,#2a2a2a)"></div><h3>BASKET BALL UNIFORM</h3><div class="mini"></div><p>Lorem ipsum dolor sit amet,<br>consectetur adipiscing elit, sed do</p><span class="btn-blue">CREATE NOW</span></div>
<div class="s-card" style="left:440px;top:3141px"><div class="ph" role="img" aria-label="Red football shirts hanging in a locker room" style="background:linear-gradient(180deg,#3a1a14,#b8302c 40%,#c94540 65%,#2f5aa8 85%,#e8d2a0)"></div><h3>FOOT BALL UNIFORM</h3><div class="mini"></div><p>Lorem ipsum dolor sit amet,<br>consectetur adipiscing elit, sed do</p><span class="btn-blue">CREATE NOW</span></div>
<div class="s-card" style="left:798px;top:3141px"><div class="ph" role="img" aria-label="Green baseball shirt on a hanger" style="background:linear-gradient(180deg,#7a8b5c,#2f5a35 45%,#1f4226 80%,#4d6040)"></div><h3>BASE BALL UNIFORM</h3><div class="mini"></div><p>Lorem ipsum dolor sit amet,<br>consectetur adipiscing elit, sed do</p><span class="btn-blue">CREATE NOW</span></div>
<div class="pager" style="left:556px;top:3714px"><span style="background:#ddd;color:#999">‹</span><span style="background:var(--red);color:#fff">›</span></div>

<div class="abs" role="img" aria-label="Two players in white and blue kits celebrating on a pitch" style="left:312px;top:3863px;width:888px;height:561px;background:linear-gradient(90deg,#cfd5c8 0%,#eef1f5 40%,#3e6a3a 100%)"></div>
<div class="circle" style="left:75px;top:3869px;width:550px;height:550px;background:linear-gradient(135deg,#fff,#cfc8c0)"></div>
<div class="circle" style="left:84px;top:3878px;width:532px;height:532px;background:var(--red)"></div>
<div class="circle-body" style="left:116px;top:3953px;width:456px">
  <h2 style="font-size:46px;font-weight:600;line-height:58px">ABOUT US</h2>
  <div style="width:80px;height:2px;background:#fff;margin:12px auto 24px"></div>
  <p>Lorem ipsum dolor sit amet, consectetur adipiscing elit, sed do eiusmod tempor incididunt ut labore et dolore magna aliqua. Quis ipsum suspendisse ultrices gravida. Risus commodo viverra maecenas accumsan lacus vel facilisis. Lorem ipsum dolor sit amet, consectetur adipiscing elit, sed do eiusmod tempor incididunt ut labore et dolore magna aliqua. Quis ipsum suspendisse ultrices gravida. Risus commodo viverra maecenas accumsan lacus vel facilisis.</p>
  <div style="margin-top:26px"><span class="btn" style="background:var(--blue);font-size:15px;padding:9px 22px">Know More ⇾</span></div>
</div>

<h2 class="sec-title" style="top:4580px;left:22px">OUR BRANDS</h2>
<div class="sec-rule" style="top:4656px;left:580px"></div>
<div class="brand-box" style="left:175px">Strider</div>
<div class="brand-box" style="left:349px">Northvale</div>
<div class="brand-box" style="left:522px">Kestrel</div>
<div class="brand-box" style="left:697px">Arcwing</div>
<div class="brand-box" style="left:872px">Tallon</div>

<footer class="site-footer">
  <div class="f-head" style="left:160px;top:90px">QUICK LINKS</div>
  <div class="f-rule" style="left:160px;top:126px"></div>
  <ul class="f-links">
    <li>Locker Room</li><li>Custom Uniforms</li><li>Custom Shirt Creator</li><li>Brands</li><li>About</li>
  </ul>
  <div class="abs" style="left:402px;top:175px;display:flex;align-items:center;gap:10px;font-size:22px;font-weight:700"><span style="width:24px;height:24px;background:var(--red)"></span>Rivet Athletic Supply</div>
  <div class="social" aria-label="Social media links"><span></span><span></span><span></span></div>
  <div class="f-head" style="left:805px;top:90px">CONTACT US</div>
  <div class="f-rule" style="left:805px;top:126px"></div>
  <div class="f-contact" style="top:163px"><span class="ci"><svg width="12" height="12" viewBox="0 0 12 12" fill="#fff"><path d="M2 1l2 0 1 3-1.5 1a7 7 0 0 0 3.5 3.5L8 7l3 1v2a1 1 0 0 1-1 1A9 9 0 0 1 1 2a1 1 0 0 1 1-1z"/></svg></span><div>CALL US<br>555 274 0186</div></div>
  <div class="f-contact" style="top:211px"><span class="ci"><svg width="12" height="10" viewBox="0 0 12 10" fill="none" stroke="#fff" stroke-width="1.3"><rect x="1" y="1" width="10" height="8"/><path d="M1 1l5 4 5-4"/></svg></span><div>EMAIL US<br>info@rivetathletic.example</div></div>
  <div class="f-contact" style="top:260px"><span class="ci"><svg width="10" height="13" viewBox="0 0 10 13" fill="#fff"><path d="M5 0a5 5 0 0 1 5 5c0 3-5 8-5 8S0 8 0 5a5 5 0 0 1 5-5zm0 3a2 2 0 1 0 0 4 2 2 0 0 0 0-4z"/></svg></span><div>Address line Dummy Here<br>Address line Here</div></div>
  <div class="abs" style="left:68px;top:341px;width:1064px;height:1px;background:rgba(255,255,255,.6)"></div>
  <div class="abs" style="left:0;top:378px;width:1200px;text-align:center;font-size:11.5px">Copyright ©2025 All rights reserved by the company name</div>
</footer>

</body>
</html>
```